Terra Swift Business Card Design

We need to improve the design of our current business card. We are a erosion control, hydro seeding company that serves many markets. We are attaching the current business card and our logo as reference. You may also visit our site at www.terraswiftllc.example to reference.

```html
<!DOCTYPE html>
<html lang="en">
<head>
<meta charset="utf-8">
<title>Terra Swift Business Card</title>
<link rel="stylesheet" href="https://fonts.googleapis.com/css2?family=Oswald:wght@500&family=Roboto:wght@400;700&display=swap">
<style>
  :root {
    --bg: #e9ece9;
    --card-white: #ffffff;
    --forest: #2f6650;
    --forest-deep: #3b6d5c;
    --leaf: #22b36b;
    --ink: #1e1e1e;
    --map: #356354;
    --on-dark: #e4efe9;
  }
  * { box-sizing: border-box; margin: 0; padding: 0; }
  html, body { width: 1200px; height: 900px; overflow: hidden; }
  body {
    background: var(--bg);
    font-family: "Roboto", Arial, sans-serif;
    display: flex;
    justify-content: center;
    align-items: center;
    gap: 80px;
  }
  .card {
    width: 400px;
    height: 700px;
    position: relative;
    overflow: hidden;
    box-shadow: 0 10px 30px rgba(0,0,0,.18);
    text-align: center;
  }
  .card--front { background: var(--card-white); color: var(--ink); }
  .card--back { background: var(--forest-deep); color: var(--on-dark); text-align: left; }

  .brand {
    display: flex;
    align-items: center;
    justify-content: center;
    gap: 10px;
    font-weight: 700;
    font-size: 40px;
    line-height: 1.2;
    letter-spacing: -0.5px;
    color: var(--forest);
  }
  .brand__dot {
    width: 22px; height: 22px; border-radius: 50%;
    background: var(--leaf);
  }
  .card--front .brand { padding-top: 60px; }
  .card--back .brand { color: #ffffff; padding-top: 60px; }

  .person { margin-top: 90px; }
  .person__name {
    font-family: "Oswald", "Arial Narrow", sans-serif;
    font-weight: 500;
    font-size: 36px;
    text-transform: uppercase;
    line-height: 1;
    color: var(--forest);
  }
  .person__name span { color: var(--leaf); }
  .person__title { font-size: 17px; margin-top: 6px; }

  .rule {
    width: 80px; height: 3px;
    background: var(--forest);
    margin: 20px auto;
  }
  .contact p, .address p { font-size: 18px; line-height: 1.3; }

  .list-heading {
    font-weight: 700;
    font-size: 32px;
    line-height: 1.2;
    color: var(--leaf);
    margin-bottom: 8px;
  }
  .markets { margin-top: 36px; }
  .markets p, .services p { font-size: 18px; line-height: 1.45; }
  .sep { color: var(--leaf); padding: 0 8px; }

  .services { padding: 56px 0 0 40px; }
  .services .list-heading { font-size: 30px; }
  .services p { font-size: 16px; }

  .coverage-map {
    position: absolute;
    left: 130px; right: 30px;
    bottom: 40px; height: 330px;
    border-radius: 60px 40px 120px 20px;
    background: var(--map);
  }
</style>
</head>
<body>
  <article class="card card--front">
    <div class="brand"><span class="brand__dot"></span>Terra Swift</div>

    <div class="person">
      <h1 class="person__name">Dale <span>Whitfield</span></h1>
      <p class="person__title">Chief Operating Officer</p>
    </div>

    <div class="rule"></div>

    <div class="contact">
      <p>(555) 301-4826</p>
      <p>(555) 301-4825</p>
      <p>info@terraswiftllc.example</p>
      <p>www.terraswiftllc.example</p>
    </div>

    <div class="rule"></div>

    <div class="address">
      <p>72 Cedar Bluff Lane Pine</p>
      <p>Hollow, NC 28000</p>
    </div>

    <section class="markets">
      <h2 class="list-heading">Markets</h2>
      <p>Solar &amp; Wind<span class="sep">|</span>Oil &amp; Gas</p>
      <p>Transformation<span class="sep">|</span>Power Plants</p>
      <p>Private Development<span class="sep">|</span>Mine Sites</p>
    </section>
  </article>

  <article class="card card--back">
    <div class="brand"><span class="brand__dot"></span>Terra Swift</div>

    <section class="services">
      <h2 class="list-heading">Services</h2>
      <p>Erosion Control<span class="sep">|</span>Seeding &amp; Matching</p>
      <p>Hydroseeding<span class="sep">|</span>Compost Blankets</p>
      <p>Site Prep<span class="sep">|</span>Renovation</p>
    </section>

    <div class="coverage-map" role="img" aria-label="Map of the eastern United States with service locations marked by stars"></div>
  </article>
</body>
</html>
```